Business Card for New Business

Please design a business card using our logo and font files. This is only one card for one person, as listed in details section.

Industry/Entity Type

Business

Contact Information for Business Card

Carl Voserby

Phone 412.318.6624
Cell 619.581.4096
Email carl@moltravex.com

www.moltravex.com

Address
18250 Brennick Lane #314
Harlow Creek, OR 97315

Font styles to use
Sans Serif

Requirements
Must have
• Information listed in detail section. Must be standard card size.

```html
<!DOCTYPE html>
<html lang="en">
<head>
<meta charset="utf-8">
<title>Moltravex Productions – Business Card</title>
<link href="https://fonts.googleapis.com/css2?family=Comfortaa:wght@300;400&family=Montserrat:wght@600&display=swap" rel="stylesheet">
<style>
  :root {
    --backdrop: #1f1f1f;
    --card-edge: #3b3b3d;
    --card-center: #56565a;
    --accent: #f0641e;
    --text-light: #d9d9d9;
  }
  * { margin: 0; padding: 0; box-sizing: border-box; }
  html, body {
    width: 1200px;
    height: 1000px;
    overflow: hidden;
    background: var(--backdrop);
  }
  .card {
    position: absolute;
    left: 75px;
    top: 200px;
    width: 1050px;
    height: 600px;
    background: radial-gradient(ellipse at 50% 45%, var(--card-center) 0%, var(--card-edge) 75%);
    box-shadow: 0 10px 30px rgba(0,0,0,0.5);
  }
  .brand {
    position: absolute;
    left: 95px;
    top: 200px;
    display: flex;
    align-items: center;
    gap: 16px;
  }
  .brand-dot {
    width: 42px;
    height: 42px;
    flex: none;
  }
  .brand-name {
    font-family: "Comfortaa", sans-serif;
    font-weight: 300;
    font-size: 50px;
    letter-spacing: 1px;
    color: var(--accent);
    line-height: 1;
    white-space: nowrap;
  }
  .rule {
    position: absolute;
    left: 0;
    right: 0;
    top: 420px;
    height: 3px;
    background: var(--accent);
  }
  .holder-name {
    position: absolute;
    left: 95px;
    top: 452px;
    font-family: "Montserrat", sans-serif;
    font-weight: 600;
    font-size: 34px;
    letter-spacing: 0.5px;
    text-transform: uppercase;
    color: var(--accent);
  }
  .contact {
    position: absolute;
    right: 60px;
    top: 292px;
    font-family: "Comfortaa", sans-serif;
    font-weight: 400;
    font-size: 21px;
    line-height: 36px;
    color: var(--text-light);
    font-style: normal;
    white-space: nowrap;
  }
</style>
</head>
<body>
  <main class="card">
    <div class="brand">
      <svg class="brand-dot" viewBox="0 0 42 42" aria-hidden="true">
        <circle cx="21" cy="21" r="21" fill="#f0641e"/>
      </svg>
      <span class="brand-name">Moltravex Productions</span>
    </div>

    <address class="contact">
      18250 Brennick Lane #314 Harlow Creek, OR 97315<br>
      412.318.6624, 619.581.4096<br>
      carl@moltravex.com, www.moltravex.com
    </address>

    <div class="rule"></div>

    <h1 class="holder-name">Carl Voserby</h1>
  </main>
</body>
</html>
```